Business Card Design Project

New Business Card design for Travorel Technology Ltd using new Logo and new Tagline for staffing company.

About us from our website - www.travorel-example.net:

TraVorel is a leading and recognized Electronic Entertainment, Workforce Augmentation, and Project Management solutions provider with clients in Electronic Entertainment, Legal, Technology, Government and other verticals that range in size from start up organizations to Zentora 300 companies. TraVorel is certified as an 8(a) minority and woman owned enterprise, established in 1998.

Target Market(s)

Companies in Electronic Entertainment, Legal, Government and Technology

Industry/Entity Type

Business

Requirements
Must have
• Must include in small letters the following information on back:

Established in 1998
8(a)(w)(e), Cage #7KQW4, DUNS #412306957

Front should have the following:
Dale Merrow
Vice President
5870 Brookhollow Court
Lindenvale, QX 908172
555-318-2046 X 100
555-742-9813 Fax
555-318-2046 Toll Free
name@travorel-example.net

Our Tagline: Connect • Collaborate • Achieve

```html
<!DOCTYPE html>
<html lang="en">
<head>
<meta charset="utf-8">
<title>TraVorel Business Card</title>
<link rel="stylesheet" href="https://fonts.googleapis.com/css2?family=Montserrat:wght@400;700&family=Arimo:wght@400;700&display=swap">
<style>
  :root {
    --stage: #1b1b1c;
    --card-top: #4a4a4d;
    --card-bottom: #0b0b0c;
    --band-top: #0c0c0d;
    --band-bottom: #3c3c3f;
    --brand-blue: #0b5cb3;
    --ink: #111111;
    --ink-soft: #555555;
    --paper: #ffffff;
    --tagline: #d9d9d9;
  }
  html, body {
    margin: 0;
    padding: 0;
    width: 750px;
    height: 1200px;
    overflow: hidden;
    background: var(--stage);
  }
  .canvas {
    position: relative;
    width: 750px;
    height: 1200px;
  }
  .card {
    position: absolute;
    left: 75px;
    width: 600px;
    height: 343px;
    overflow: hidden;
    box-shadow: 0 12px 30px rgba(0,0,0,0.6);
  }

  /* Front */
  .card-front {
    top: 170px;
    background: linear-gradient(180deg, var(--card-top) 0%, #1e1e20 55%, var(--card-bottom) 100%);
  }
  .brand {
    display: flex;
    align-items: center;
    gap: 14px;
    font-family: "Montserrat", sans-serif;
    font-weight: 700;
    color: var(--paper);
  }
  .brand-dot {
    flex: none;
    border-radius: 50%;
    background: var(--brand-blue);
  }
  .card-front .brand {
    position: absolute;
    left: 0;
    right: 0;
    top: 118px;
    justify-content: center;
    font-size: 62px;
    line-height: 1;
  }
  .card-front .brand-dot { width: 30px; height: 30px; }
  .tagline {
    position: absolute;
    left: 0;
    right: 0;
    bottom: 34px;
    margin: 0;
    text-align: center;
    font-family: "Montserrat", sans-serif;
    font-weight: 400;
    font-size: 15px;
    letter-spacing: 1px;
    color: var(--tagline);
  }

  /* Back */
  .card-back {
    top: 650px;
    background: var(--paper);
  }
  .card-band {
    position: absolute;
    left: 0;
    top: 0;
    width: 100%;
    height: 140px;
    background: linear-gradient(180deg, var(--band-top) 0%, #1d1d1f 55%, var(--band-bottom) 100%);
  }
  .card-back .brand {
    position: absolute;
    left: 40px;
    top: 40px;
    font-size: 32px;
    line-height: 1;
    gap: 10px;
  }
  .card-back .brand-dot { width: 16px; height: 16px; }
  .contact {
    position: absolute;
    right: 58px;
    top: 116px;
    margin: 0;
    text-align: right;
    font-family: "Arimo", sans-serif;
    font-size: 16px;
    line-height: 19px;
    color: var(--ink);
    font-style: normal;
  }
  .contact-name {
    display: block;
    font-weight: 700;
    color: var(--paper);
    margin-bottom: 5px;
  }
  .contact-line { display: block; }
  .fine-print {
    position: absolute;
    left: 40px;
    bottom: 22px;
    margin: 0;
    font-family: "Arimo", sans-serif;
    font-size: 10px;
    line-height: 14px;
    color: var(--ink-soft);
  }
  .fine-print span { display: block; }
  .accent-tab {
    position: absolute;
    right: 44px;
    bottom: 0;
    width: 168px;
    height: 44px;
    background: var(--brand-blue);
    border-radius: 10px 10px 0 0;
  }
</style>
</head>
<body>
  <main class="canvas">
    <section class="card card-front" aria-label="Card front">
      <div class="brand">
        <span class="brand-dot"></span>
        <span class="brand-name">TraVorel</span>
      </div>
      <p class="tagline">CONNECT • COLLABORATE • ACHIEVE</p>
    </section>

    <section class="card card-back" aria-label="Card back">
      <div class="card-band"></div>
      <div class="brand">
        <span class="brand-dot"></span>
        <span class="brand-name">TraVorel</span>
      </div>
      <address class="contact">
        <span class="contact-name">Dale Merrow</span>
        <span class="contact-line">Vice President</span>
        <span class="contact-line">5870 Brookhollow Court</span>
        <span class="contact-line">Lindenvale, QX 908172</span>
        <span class="contact-line">555-318-2046 X 100</span>
        <span class="contact-line">555-742-9813 Fax</span>
        <span class="contact-line">555-318-2046 Toll Free</span>
        <span class="contact-line">name@travorel-example.net</span>
      </address>
      <p class="fine-print">
        <span>Established in 1998</span>
        <span>8(a)(w)(e), Cage #7KQW4, DUNS #412306957</span>
      </p>
      <div class="accent-tab"></div>
    </section>
  </main>
</body>
</html>
```